Business Card Design

I need a business card designed for my new company BrightOak Home developments I specialise in all aspects of carpentry including Decks, Pergolas, Conventional Framing and fit outs I am open to different colours as long as it fits with my logo.

Industry/Entity Type

Carpentry

Contact Information for Business Card

BrightOak Home Developments, Rob Keltmore, 0481604328, specialising in all aspects of carpentry and construction

```html
<!DOCTYPE html>
<html lang="en">
<head>
<meta charset="utf-8">
<title>BrightOak Home Developments – Business Card</title>
<link href="https://fonts.googleapis.com/css2?family=Ubuntu:ital,wght@0,400;0,500;0,700;1,700&display=swap" rel="stylesheet">
<style>
  :root {
    --brand-blue: #2b4f8d;
    --card-white: #f4f4f5;
    --backdrop: #e9e9ea;
    --panel-text: #eef2f8;
  }
  * { box-sizing: border-box; margin: 0; padding: 0; }
  html, body {
    width: 1200px; height: 952px; overflow: hidden;
    background: var(--backdrop);
    font-family: "Ubuntu", sans-serif;
    color: var(--brand-blue);
  }
  .stage { position: relative; width: 1200px; height: 952px; }

  .card {
    position: absolute;
    width: 540px; height: 310px;
    background: var(--card-white);
    box-shadow: 0 6px 18px rgba(0,0,0,0.10);
    overflow: hidden;
  }

  /* Front: brand card */
  .card--front { left: 580px; top: 110px; }
  .card--front .edge-stripe {
    position: absolute; left: 0; right: 0; height: 7px; background: var(--brand-blue);
  }
  .card--front .edge-stripe--top { top: 0; }
  .card--front .edge-stripe--bottom { bottom: 0; }
  .brand-lockup {
    position: absolute; left: 0; right: 0; top: 50%;
    transform: translateY(-50%);
    display: flex; align-items: center; justify-content: center; gap: 16px;
  }
  .brand-mark {
    width: 18px; height: 18px; background: var(--brand-blue);
  }
  .brand-name {
    font-weight: 400; color: var(--brand-blue); line-height: 1.1;
  }
  .brand-name__primary { display: block; font-size: 38px; letter-spacing: 1px; }
  .brand-name__secondary { display: block; font-size: 15px; letter-spacing: 4px; text-transform: uppercase; }

  /* Back: contact card */
  .card--back { left: 100px; top: 520px; }
  .brand-panel {
    position: absolute; left: 0; top: 0; bottom: 0; width: 170px;
    background: var(--brand-blue);
    display: flex; align-items: center; justify-content: center;
  }
  .brand-panel .brand-name {
    color: var(--panel-text); text-align: center;
  }
  .brand-panel .brand-name__primary { font-size: 21px; letter-spacing: 0.5px; }
  .brand-panel .brand-name__secondary { font-size: 9px; letter-spacing: 2px; margin-top: 4px; }
  .right-stripe {
    position: absolute; right: 0; top: 0; bottom: 0; width: 8px; background: var(--brand-blue);
  }
  .contact {
    position: absolute; left: 200px; top: 34px; right: 30px;
  }
  .contact__name { font-size: 19px; font-weight: 700; }
  .contact__phone {
    display: flex; align-items: center; gap: 10px;
    margin-top: 10px; font-size: 15px; font-weight: 400;
  }
  .contact__phone svg { width: 16px; height: 16px; }
  .specialty { position: absolute; left: 200px; top: 178px; right: 30px; }
  .specialty__label { font-size: 16px; font-weight: 700; font-style: italic; }
  .specialty__text { font-size: 16px; font-weight: 400; margin-top: 6px; }
</style>
</head>
<body>
<main class="stage">

  <section class="card card--front" aria-label="Business card front">
    <div class="edge-stripe edge-stripe--top"></div>
    <div class="brand-lockup">
      <span class="brand-mark" aria-hidden="true"></span>
      <p class="brand-name">
        <span class="brand-name__primary">BrightOak</span>
        <span class="brand-name__secondary">Home Developments</span>
      </p>
    </div>
    <div class="edge-stripe edge-stripe--bottom"></div>
  </section>

  <section class="card card--back" aria-label="Business card back">
    <div class="brand-panel">
      <p class="brand-name">
        <span class="brand-name__primary">BrightOak</span>
        <span class="brand-name__secondary">Home Developments</span>
      </p>
    </div>

    <div class="contact">
      <h1 class="contact__name">Rob Keltmore</h1>
      <p class="contact__phone">
        <svg viewBox="0 0 16 16" aria-hidden="true">
          <circle cx="8" cy="8" r="8" fill="#2b4f8d"/>
          <path d="M5.6 4.2c.3-.2.7-.1.9.2l.8 1.3c.2.3.1.6-.1.8l-.5.4c.4.9 1.1 1.7 2 2.1l.4-.5c.2-.2.6-.3.8-.1l1.3.8c.3.2.4.6.2.9l-.4.6c-.3.4-.8.6-1.3.5C7.6 10.7 5.3 8.4 4.8 6.3c-.1-.5.1-1 .5-1.3z" fill="#f4f4f5"/>
        </svg>
        048-160-4328
      </p>
    </div>

    <div class="specialty">
      <p class="specialty__label">Specialising in :</p>
      <p class="specialty__text">All aspects of carpentry &amp; construction</p>
    </div>

    <div class="right-stripe"></div>
  </section>

</main>
</body>
</html>
```